business card with logo

Would like a business card for an electrical contractor called BRANNOCK ELECTRICS.
No generic electrical imagery (light globe, powerpoints, ect). Would like a logo or symbol created in the design as part of the project . I would like crisp colour. No templated designs like Dorvex

is there any other designers willing to submit designs

Electrical

```html
<!DOCTYPE html>
<html lang="en">
<head>
<meta charset="utf-8">
<title>Brannock Electrics – Business Card</title>
<link rel="stylesheet" href="https://fonts.googleapis.com/css2?family=PT+Sans:wght@400;700&family=PT+Sans+Narrow:wght@400&display=swap">
<style>
  :root {
    --backdrop: #353334;
    --brand-orange: #f06a38;
    --brand-slate: #637079;
    --paper: #ffffff;
    --text-grey: #5a5a5a;
    --faint-slate: #cfd4d8;
    --faint-orange: #fbd6c8;
  }
  * { margin: 0; padding: 0; box-sizing: border-box; }
  html, body { width: 1200px; height: 750px; overflow: hidden; background: var(--backdrop); }
  .canvas { position: relative; width: 1200px; height: 750px; font-family: "PT Sans", Arial, sans-serif; }

  .logo-panel {
    position: absolute; top: 41px; height: 326px;
    display: flex; align-items: center; justify-content: center;
  }
  .logo-panel--orange { left: 42px; width: 557px; background: var(--brand-orange); }
  .logo-panel--white { left: 599px; width: 558px; background: var(--paper); }

  .wordmark {
    font-weight: 700; text-align: center; line-height: 1;
    margin-top: -30px;
  }
  .wordmark__main { display: block; font-size: 50px; letter-spacing: 1px; }
  .wordmark__sub { display: block; font-size: 19px; letter-spacing: 7px; margin-top: 8px; }
  .logo-panel--orange .wordmark { color: var(--paper); }
  .logo-panel--white .wordmark { color: var(--brand-slate); }

  .card {
    position: absolute; left: 321px; top: 381px; width: 558px; height: 327px;
    background: var(--paper); overflow: hidden;
  }
  .card__decor { position: absolute; right: 0; bottom: 0; }
  .card__name {
    position: absolute; left: 40px; top: 44px;
    font-family: "PT Sans Narrow", "Arial Narrow", sans-serif;
    font-size: 42px; color: var(--brand-orange); line-height: 1;
  }
  .card__role {
    position: absolute; left: 41px; top: 90px;
    font-family: "PT Sans Narrow", "Arial Narrow", sans-serif;
    font-size: 19px; color: var(--text-grey);
  }
  .card__details {
    position: absolute; left: 41px; top: 132px;
    font-family: "PT Sans Narrow", "Arial Narrow", sans-serif;
    font-size: 13.5px; line-height: 16px; color: var(--text-grey);
    font-style: normal;
  }
  .card__details p + p { margin-top: 15px; }
  .card__social { display: flex; gap: 18px; margin-top: 17px; }
  .card__social span { display: inline-flex; align-items: center; gap: 8px; }
  .card__social i { display: inline-block; width: 11px; height: 11px; background: var(--brand-orange); }
</style>
</head>
<body>
<main class="canvas">
  <section class="logo-panel logo-panel--orange">
    <div class="wordmark"><span class="wordmark__main">BRANNOCK</span><span class="wordmark__sub">ELECTRICS</span></div>
  </section>
  <section class="logo-panel logo-panel--white">
    <div class="wordmark"><span class="wordmark__main">BRANNOCK</span><span class="wordmark__sub">ELECTRICS</span></div>
  </section>

  <article class="card">
    <svg class="card__decor" width="210" height="160" viewBox="0 0 210 160" aria-hidden="true">
      <rect x="20" y="10" width="190" height="150" fill="var(--faint-slate)" opacity="0.55"/>
      <rect x="20" y="95" width="85" height="65" fill="var(--faint-orange)"/>
    </svg>
    <h1 class="card__name">Liam Carverly</h1>
    <p class="card__role">Co-Founder</p>
    <address class="card__details">
      <p>27 Harrow Bend<br>Port Kellan, WA 6999<br>9581.4402 (t)<br>041.327.8845 (m)</p>
      <p>liam@brannockelectrics.com<br>http://www.brannockelectrics.com</p>
      <div class="card__social">
        <span><i></i>brannockelec</span>
        <span><i></i>brannockelec</span>
      </div>
    </address>
  </article>
</main>
</body>
</html>
```